Pull Up Banner - Recruitment Company

We would like a design for a pull up banner.

For context: we are a recruitment business. We specialise in helping people in healthcare industry to find jobs in Australia.

I have come up with several ideas and text for the banner. Feel free to use the following as you see appropriate:

- Our logo (see attached)
- 'Healthcare Recruitment Agency'
- Some sort of imagine / cartoon of medical professionals (ie. doctor, nurse, physiotherapist, speech pathologist). A cartoon is more friendly than committing to a photo
- 'Empowering your next career move'
- 'Discover tailored opportunities based on your career preferences'
- Dot points (allied health, nursing, medical imaging)
- Contact info at the bottom including our website (www.quellstaffing.com.au, our Instagram handle @quellstaffing, Mobile: XXXX XXX XXX. The title section for contact information could be 'Get in touch:'

Feel free to submit a couple of designs and we can merge aspects that look good on your designs and find the perfect fit.
Thank you
Updates

Hello,

Thank you for your initial submissions to this project. I appreciate the time you've invested.

After reviewing the first attempt, I'd like to share some feedback and initial observations:

- Professionalism and engagement: Is the overall appearance of the banner professional? It's crucial that we have a high-quality design as this will represent our business.

- Image selection: The image (whether cartoon or real people) appears quite generic. Please consider submitting the banner with a few different photos in the middle for us to choose from. Ensure the image is a good fit and not simply a generic stock photo.

- Contact section: Kindly remove the phone number; we no longer wish to include it on the banner. Instead, please include our website (www.quellstaffing.com.au) and Instagram handle (@quellstaffing).

- Color scheme: White, black, and red/pink are preferred, or alternatively, blue. However, please avoid incorporating too many different colors as it may detract from the professional appearance.

We will be printing the design on a banner and require it to look professional and engaging.

Thank you once again for your submissions. I hope the feedback provided above is helpful.

Warm regards,

Target Market(s)

Allied Health Australia

Font styles to use
Serif

Colors
0054AA
0677BA
7BADD7
CADEEF
E8F1F8
0094D4
00A9DD
6FCCEA
C7EBF8
E9F6FB
EB3D1F
EC4F4E
F09395
F8D3D4
FCEDEE

```html
<!DOCTYPE html>
<html lang="en">
<head>
<meta charset="utf-8">
<title>Quell Staffing – Healthcare Recruitment Agency Pull Up Banner</title>
<link rel="stylesheet" href="https://fonts.googleapis.com/css2?family=League+Spartan:wght@400;800&family=Poppins:wght@500;600;700&family=Montserrat:wght@700&display=swap">
<style>
  :root {
    --royal: #0b1486;
    --navy: #09105c;
    --bright: #3542d6;
    --sky: #6f95f0;
    --ice: #e4eefb;
    --ice-deep: #b9cff0;
    --accent: #1f80e8;
    --ink: #232323;
    --paper: #ffffff;
    --bar: #1b1b1b;
  }
  * { margin: 0; padding: 0; box-sizing: border-box; }
  html, body { width: 1200px; height: 2400px; overflow: hidden; background: var(--paper); }
  .banner { position: relative; width: 1200px; height: 2400px; overflow: hidden; }
  .backdrop { position: absolute; inset: 0; }

  .brand { position: absolute; top: 95px; left: 0; width: 1200px; text-align: center; color: var(--paper);
    font-family: "Montserrat", sans-serif; font-weight: 700; }
  .brand-name { font-size: 118px; letter-spacing: 10px; line-height: 1; }
  .brand-sub { font-size: 32px; letter-spacing: 9px; margin-top: 18px; }

  .headline { position: absolute; top: 330px; left: 0; width: 1200px; text-align: center;
    font-family: "League Spartan", sans-serif; font-weight: 800; line-height: 0.92; }
  .headline .lead { display: block; color: var(--sky); font-size: 104px; }
  .headline .main { display: block; color: var(--paper); font-size: 124px; }

  .tagline { position: absolute; top: 1596px; left: 0; width: 1200px; text-align: center;
    font-family: "League Spartan", sans-serif; color: var(--ink); line-height: 1; }
  .tagline .light { display: block; font-weight: 400; font-size: 74px; }
  .tagline .bold { display: block; font-weight: 800; font-size: 74px; margin-top: 8px; }

  .discover { position: absolute; top: 1768px; left: 0; width: 1200px; text-align: center;
    font-family: "Poppins", sans-serif; font-weight: 600; font-size: 42px; letter-spacing: 20px; color: var(--accent); }
  .offer { position: absolute; top: 1822px; left: 0; width: 1200px; text-align: center;
    font-family: "Poppins", sans-serif; font-weight: 600; font-size: 44px; line-height: 1.25; color: var(--ink); }

  .sectors { position: absolute; top: 1970px; left: 70px; width: 1060px; display: flex; justify-content: center; }
  .sector { display: flex; flex-direction: column; align-items: center; padding: 0 38px;
    font-family: "Poppins", sans-serif; font-weight: 500; font-size: 38px; color: var(--ink); }
  .sector + .sector { border-left: 2px solid #cfcfcf; }
  .sector svg { width: 64px; height: 64px; margin-bottom: 14px; }

  .web { position: absolute; top: 2145px; left: 116px; width: 984px; height: 88px; border-radius: 18px;
    background: var(--bar); color: var(--paper); text-align: center; line-height: 88px;
    font-family: "Poppins", sans-serif; font-weight: 700; font-size: 46px; letter-spacing: 3px; }
  .social { position: absolute; top: 2250px; left: 0; width: 1200px; text-align: center;
    font-family: "Poppins", sans-serif; font-weight: 500; font-size: 46px; color: var(--ink); }
  .social .dot { display: inline-block; width: 34px; height: 34px; border-radius: 50%; background: #e8437a;
    vertical-align: -4px; margin: 0 8px 0 6px; }
</style>
</head>
<body>
<main class="banner">
  <svg class="backdrop" width="1200" height="2400" viewBox="0 0 1200 2400">
    <rect width="1200" height="2400" fill="var(--royal)"/>
    <polygon points="0,645 620,1010 0,1230" fill="var(--navy)"/>
    <polygon points="1200,620 600,980 1200,1160" fill="var(--bright)"/>
    <polygon points="0,1180 620,1540 0,1660" fill="var(--bright)"/>
    <polygon points="1200,1060 600,1520 1200,1580" fill="var(--navy)"/>
    <polygon points="0,1660 600,1420 1200,1585 1200,2400 0,2400" fill="var(--paper)"/>
    <defs>
      <linearGradient id="sceneTone" x1="0" y1="0" x2="0" y2="1">
        <stop offset="0" stop-color="#9bb8ec"/>
        <stop offset="1" stop-color="var(--ice)"/>
      </linearGradient>
    </defs>
    <polygon class="illustration" role="img" aria-label="Isometric illustration of healthcare staff beside a medical shield, patient data screens and file binders"
      points="600,700 1200,1073 600,1491 0,1073" fill="url(#sceneTone)"/>
  </svg>

  <header class="brand">
    <div class="brand-name">QUELL</div>
    <div class="brand-sub">STAFFING</div>
  </header>

  <h1 class="headline">
    <span class="lead">HEALTHCARE</span>
    <span class="main">RECRUITMENT</span>
    <span class="main">AGENCY</span>
  </h1>

  <h2 class="tagline">
    <span class="light">EMPOWERING YOUR</span>
    <span class="bold">NEXT CAREER MOVE</span>
  </h2>

  <p class="discover">DISCOVER</p>
  <p class="offer">tailored opportunities based on your<br>career preferences</p>

  <ul class="sectors">
    <li class="sector">
      <svg viewBox="0 0 64 64" aria-hidden="true">
        <path d="M32 50 L12 30 A10 10 0 0 1 32 16 A10 10 0 0 1 52 30 Z" fill="var(--royal)"/>
        <polyline points="14,32 24,32 28,24 34,40 38,32 50,32" fill="none" stroke="#fff" stroke-width="3"/>
      </svg>
      Allied health
    </li>
    <li class="sector">
      <svg viewBox="0 0 64 64" aria-hidden="true">
        <rect x="12" y="12" width="40" height="40" rx="8" fill="var(--royal)"/>
        <rect x="28" y="20" width="8" height="24" fill="#fff"/>
        <rect x="20" y="28" width="24" height="8" fill="#fff"/>
      </svg>
      Nursing
    </li>
    <li class="sector">
      <svg viewBox="0 0 64 64" aria-hidden="true">
        <circle cx="30" cy="28" r="18" fill="none" stroke="var(--royal)" stroke-width="7"/>
        <rect x="22" y="38" width="36" height="8" fill="var(--bar)"/>
        <rect x="26" y="48" width="6" height="10" fill="var(--royal)"/>
      </svg>
      Medical imaging
    </li>
  </ul>

  <div class="web">www.quellstaffing.com.au</div>
  <p class="social">Follow us at <span class="dot"></span>@quellstaffing</p>
</main>
</body>
</html>
```